Web Site Design for a Finance (lending) Company

We are opening a new subsidiary that focuses on lending money in the real estate industry. We need a web site designed to represent the business.

The business is lending money to real estate investors. A typical client/borrower will be looking to borrow money to buy a house, renovate it and then sell it at a profit, all within 12 months or less.

Company name is Varlo Finance. Our logo is attached.

Attached is a general outline for the web site. We're working on writing more text for each page but this should give you enough to get started with some ideas.

Competitor web site that I like a lot (as an example): https://brixhallfunding.example/. Many of the general items on this site match what we will need (description of loan programs, FAQ)

Target Market(s)

Real estate investors (generally individuals or small companies with just a few people) who are buying homes, renovating them and then selling them at a profit.

Industry/Entity Type

Finance

Coding

Coded - Design and coding required

Number of Pages Required

5+ page

Colors

Designer to choose colors to be used in the design.

Requirements
Must have
• Minimalist design. Clean lines without too much clutter. Some stock photography is ok but the photos should not be distracting. They should almost fade in to the background so that user can focus on the key information about what our company does instead. We are a finance company, not a design company, so the information about our products will be more interesting to site visitors than the art.
• Some minimalist examples from Mosaiko:
• https://www.mosaiko.example/explore/minimalist-web-design/
Nice to have
• If you search in searchly for "hard money lenders" you will find many examples of web sites from our competition. I have provided a link above to competitor web site that I like a lot.
• I have attached our logo in EPS format. Logo is green. Web site doesn't have to be green but it should be of a color that will work well with the logo.

```html
<!DOCTYPE html>
<html lang="en">
<head>
<meta charset="UTF-8">
<title>Varlo Finance – Team &amp; Loans</title>
<link rel="stylesheet" href="https://fonts.googleapis.com/css2?family=Questrial&family=Figtree:wght@400&display=swap">
<style>
  :root {
    --ink: #161616;
    --gold: #a0712f;
    --gold-line: #b8893f;
    --grey-line: #6a6a6a;
    --cream: #faf5ef;
    --paper: #ffffff;
    --intro-bg: #fdfcfb;
    --white: #ffffff;
  }
  * { margin: 0; padding: 0; box-sizing: border-box; }
  html, body { width: 1040px; height: 1200px; overflow: hidden; background: var(--paper); }
  body { position: relative; font-family: "Questrial", sans-serif; color: var(--ink); }
  h2, h3 { font-weight: 400; }

  .intro { position: absolute; left: 0; top: 0; width: 480px; height: 166px; background: var(--intro-bg); }
  .intro-text {
    position: absolute; left: 52px; top: -8px; width: 422px;
    font-size: 14.4px; line-height: 17.3px; letter-spacing: 2.5px; color: #3a3a3a;
  }
  .btn-more {
    position: absolute; left: 324px; top: 122px; width: 126px; height: 32px;
    border: 1px solid var(--gold); border-radius: 16px;
    font-size: 12px; letter-spacing: 2.2px; line-height: 30px; text-align: center; color: var(--ink);
  }
  .photo { position: absolute; }
  .photo-target { left: 519px; top: 0; width: 261px; height: 166px;
    background: linear-gradient(135deg, #8a8880 0%, #5d5f5e 45%, #3f4345 100%); }
  .photo-arrow { left: 780px; top: 0; width: 260px; height: 166px;
    background: linear-gradient(135deg, #4b4d50 0%, #3c3e41 45%, #5a5338 65%, #3a3c3f 100%); }

  .section-title { position: absolute; letter-spacing: 6px; }
  .team-title { left: 50px; top: 284px; font-size: 42px; }
  .team-title .accent { color: var(--gold); }

  .team-cell { position: absolute; width: 260px; height: 260px; }
  .team-card { background: var(--cream); }
  .team-photo { box-shadow: 0 2px 3px rgba(0,0,0,.25); }
  .card-rule { position: absolute; height: 1px; width: 46px; background: var(--gold-line); }
  .card-rule-grey { background: var(--grey-line); }
  .card-name { position: absolute; font-size: 19px; letter-spacing: 2.6px; white-space: nowrap; }
  .card-bio {
    position: absolute; width: 170px;
    font-family: "Figtree", sans-serif; font-size: 14.2px; line-height: 17.4px; color: #222;
  }

  .loans-title { left: 0; width: 1040px; text-align: center; top: 946px; font-size: 40px; letter-spacing: 7px; padding-left: 7px; }
  .divider { position: absolute; left: 448px; top: 1002px; }

  .loan-panel { position: absolute; top: 1106px; height: 94px; width: 520px; overflow: hidden; }
  .loan-flip { left: 0; background: linear-gradient(160deg, #5f4a36 0%, #7c5f42 40%, #86684a 100%); }
  .loan-commercial { left: 520px; background: linear-gradient(160deg, #284228 0%, #2f4e30 50%, #36563a 100%); }
  .loan-name { position: absolute; color: var(--white); font-size: 32px; letter-spacing: 4px; white-space: nowrap; }
</style>
</head>
<body>

  <section class="intro">
    <p class="intro-text">consectetur adipiscing elit. Aliquam quis varius ante. Etiam ornare, justo a cursus hendrerit, ex sapien consectetur eros, non dictum ex ex vel quam. Nam metus justo,</p>
    <div class="btn-more">READ MORE</div>
  </section>
  <div class="photo photo-target" role="img" aria-label="Close-up photo of a dart hitting a target board"></div>
  <div class="photo photo-arrow" role="img" aria-label="Photo of a hand drawing a yellow chalk arrow on asphalt"></div>

  <h2 class="section-title team-title">OUR <span class="accent">TEAM</span></h2>

  <div class="team-cell team-photo" style="left:0;top:342px;background:linear-gradient(120deg,#e4e4e2,#bdbdbb 60%,#6b6b6b);" role="img" aria-label="Black and white portrait of a team member"></div>
  <div class="team-cell team-card" style="left:260px;top:342px;">
    <h3 class="card-name" style="left:54px;top:62px;">LOREM IPSUM</h3>
    <p class="card-bio" style="left:56px;top:98px;">Lorem ipsum dolor sit amet, consectetur adipiscing elit. Aliquam quis varius ante</p>
  </div>
  <div class="card-rule" style="left:245px;top:373px;"></div>

  <div class="team-cell team-photo" style="left:520px;top:342px;background:linear-gradient(160deg,#3a3b3d,#485063 45%,#6a6431 80%,#3c3c3c);" role="img" aria-label="Portrait of a team member writing in a notebook"></div>
  <div class="team-cell team-card" style="left:780px;top:342px;">
    <h3 class="card-name" style="left:54px;top:56px;">LOREM IPSUM</h3>
    <p class="card-bio" style="left:56px;top:92px;">Lorem ipsum dolor sit amet, consectetur adipiscing elit. Aliquam quis varius ante</p>
  </div>
  <div class="card-rule" style="left:765px;top:373px;"></div>

  <div class="team-cell team-card" style="left:0;top:606px;">
    <h3 class="card-name" style="left:54px;top:62px;">LOREM IPSUM</h3>
    <p class="card-bio" style="left:56px;top:98px;">Lorem ipsum dolor sit amet, consectetur adipiscing elit. Aliquam quis varius ante</p>
  </div>
  <div class="team-cell team-photo" style="left:260px;top:606px;background:linear-gradient(110deg,#d9675a,#3f8aa0 35%,#a06a4a 65%,#6b4630);" role="img" aria-label="Portrait of a team member in front of a colourful mural"></div>
  <div class="card-rule card-rule-grey" style="left:230px;top:636px;"></div>

  <div class="team-cell team-card" style="left:520px;top:606px;">
    <h3 class="card-name" style="left:54px;top:62px;">LOREM IPSUM</h3>
    <p class="card-bio" style="left:56px;top:98px;">Lorem ipsum dolor sit amet, consectetur adipiscing elit. Aliquam quis varius ante</p>
  </div>
  <div class="team-cell team-photo" style="left:780px;top:606px;background:linear-gradient(150deg,#1c1c1c,#2a2a2a 40%,#6e6e6e 70%,#1a1a1a);" role="img" aria-label="Black and white portrait of a smiling team member"></div>
  <div class="card-rule card-rule-grey" style="left:750px;top:636px;"></div>

  <h2 class="section-title loans-title">LOANS</h2>
  <svg class="divider" width="144" height="20" viewBox="0 0 144 20" aria-hidden="true">
    <line x1="2" y1="9" x2="56" y2="9" stroke="#222" stroke-width="1"/>
    <line x1="87" y1="9" x2="141" y2="9" stroke="#222" stroke-width="1"/>
    <polyline points="64,2 71,9 64,16" fill="none" stroke="#a0712f" stroke-width="1.8"/>
    <polyline points="70,2 77,9 70,16" fill="none" stroke="#a0712f" stroke-width="1.8"/>
  </svg>

  <section class="loan-panel loan-flip" role="img" aria-label="Muted brown landscape photo behind the fix and flip loans title">
    <h3 class="loan-name" style="left:84px;top:73px;">FIX AND FLIP LOANS</h3>
  </section>
  <section class="loan-panel loan-commercial" role="img" aria-label="Muted green textured photo behind the commercial hard money title">
    <h3 class="loan-name" style="left:90px;top:52px;">COMMERCIAL HARD</h3>
  </section>

</body>
</html>
```